Cash Flow Slide Design

Help Make Slide flow, FT Arrow to paying Down HELOC Then Bring in new Home Purchase and look amazing.
Serif
EB3D1F
EC4F4E
F09395
F8D3D4
FCEDEE

```html
<!DOCTYPE html>
<html lang="en">
<head>
<meta charset="utf-8">
<title>Wealth Builder Account – Cash Flow Slides</title>
<link rel="stylesheet" href="https://fonts.googleapis.com/css2?family=Poppins:ital,wght@0,600;0,700;0,800;1,700;1,800&display=swap">
<style>
  :root {
    --page-bg: #e8e8e8;
    --slide-bg: #ffffff;
    --navy: #112c72;
    --navy-deep: #0e2057;
    --ink: #111111;
    --green-text: #1db040;
    --arrow-blue: #3d6bde;
    --arrow-tip: #2a4fb3;
    --white: #ffffff;
  }
  * { box-sizing: border-box; margin: 0; padding: 0; }
  html, body {
    width: 1021px; height: 1200px; overflow: hidden;
    background: var(--page-bg);
    font-family: "Poppins", sans-serif;
  }
  .slide {
    position: absolute; left: 75px; width: 871px; height: 490px;
    background: var(--slide-bg);
    box-shadow: 0 2px 4px rgba(0,0,0,.35);
  }
  .slide--first { top: 83px; }
  .slide--second { top: 627px; }
  .slide-header {
    height: 64px; background: var(--navy);
    display: flex; align-items: center; justify-content: space-between;
    padding: 0 36px 0 66px;
  }
  .slide-title {
    color: var(--white); font-weight: 800; font-size: 29px; letter-spacing: -0.2px;
  }
  .brand {
    color: var(--white); font-weight: 700; font-size: 18px;
  }
  .flow { display: block; width: 871px; height: 426px; }
  .t-heading { font-weight: 800; font-size: 38px; fill: var(--ink); }
  .t-green { fill: var(--green-text); }
  .t-label { font-weight: 800; font-size: 29px; fill: var(--ink); }
  .t-arrow { font-weight: 700; font-size: 16px; fill: var(--white); }
  .t-arrow-sm { font-weight: 700; font-size: 13px; fill: var(--white); }
  .t-ft { font-weight: 800; font-size: 26px; fill: var(--white); }
  .t-column { font-weight: 800; font-style: italic; font-size: 19px; fill: var(--ink); }
  .t-home { font-weight: 800; font-size: 38px; fill: var(--white); }
  .t-home-label { font-weight: 800; font-size: 38px; fill: var(--navy); }
  .plate-top { fill: #dcdcdc; }
  .plate-side { fill: #bdbdbd; }
</style>
</head>
<body>

<section class="slide slide--first">
  <header class="slide-header">
    <h1 class="slide-title">Wealth Builder Account</h1>
    <div class="brand">Northwise Financial</div>
  </header>
  <svg class="flow" viewBox="0 0 1505 740" xmlns="http://www.w3.org/2000/svg">
    <defs>
      <linearGradient id="house-tone" x1="0" y1="0" x2="0" y2="1">
        <stop offset="0" stop-color="#cfe4f5"/>
        <stop offset="0.55" stop-color="#d99a84"/>
        <stop offset="1" stop-color="#5e9a4a"/>
      </linearGradient>
      <radialGradient id="bubble" cx="0.5" cy="0.45" r="0.6">
        <stop offset="0" stop-color="#ffffff"/>
        <stop offset="1" stop-color="#e6e6e6"/>
      </radialGradient>
    </defs>

    <g id="shared-flow">
      <text class="t-heading" x="721" y="50" text-anchor="middle">Offset Account: <tspan class="t-green">Permanent Life Insurance</tspan></text>

      <g class="icon icon--checking">
        <circle cx="256" cy="115" r="38" fill="#5aa84a"/>
        <rect x="241" y="97" width="26" height="34" rx="3" fill="none" stroke="#fff" stroke-width="3"/>
        <line x1="247" y1="108" x2="261" y2="108" stroke="#fff" stroke-width="3"/>
        <line x1="247" y1="116" x2="256" y2="116" stroke="#fff" stroke-width="3"/>
        <circle cx="266" cy="124" r="7" fill="#5aa84a" stroke="#fff" stroke-width="3"/>
      </g>
      <g class="icon icon--insurance">
        <circle cx="595" cy="115" r="38" fill="#f6c000"/>
        <path d="M595 96 l14 5 v9 c0 9-6 15-14 18 c-8-3-14-9-14-18 v-9z" fill="none" stroke="#222" stroke-width="3"/>
        <path d="M578 132 h14 l10-4" fill="none" stroke="#222" stroke-width="3"/>
      </g>
      <g class="icon icon--heloc">
        <circle cx="928" cy="115" r="38" fill="#cc1111"/>
        <circle cx="935" cy="103" r="7" fill="none" stroke="#fff" stroke-width="3"/>
        <rect x="925" y="114" width="20" height="12" fill="none" stroke="#fff" stroke-width="3"/>
        <path d="M908 126 h14 l12 6" fill="none" stroke="#fff" stroke-width="3"/>
      </g>

      <text class="t-label" x="256" y="185" text-anchor="middle">Checking</text>
      <text class="t-label" x="595" y="185" text-anchor="middle">OA <tspan class="t-green">Life Insurance</tspan></text>
      <text class="t-label" x="928" y="185" text-anchor="middle">HELOC</text>

      <g class="plates">
        <polygon class="plate-side" points="115,620 252,688 389,620 389,633 252,701 115,633"/>
        <polygon class="plate-side" points="454,620 591,688 728,620 728,633 591,701 454,633"/>
        <polygon class="plate-side" points="791,620 928,688 1065,620 1065,633 928,701 791,633"/>
        <polygon class="plate-side" points="1129,620 1266,688 1403,620 1403,633 1266,701 1129,633"/>
        <polygon class="plate-top" points="115,620 252,552 389,620 252,688"/>
        <polygon class="plate-top" points="454,620 591,552 728,620 591,688"/>
        <polygon class="plate-top" points="791,620 928,552 1065,620 928,688"/>
        <polygon class="plate-top" points="1129,620 1266,552 1403,620 1266,688"/>
      </g>

      <g class="column column--checking">
        <polygon points="145,245 252,300 252,678 145,625" fill="#c0dca8"/>
        <polygon points="252,300 359,245 359,625 252,678" fill="#93c072"/>
        <polygon points="252,195 359,245 252,300 145,245" fill="#70ad47"/>
        <polygon points="145,407 252,460 252,620 145,567" fill="#6fab47"/>
        <polygon points="252,460 359,407 359,567 252,620" fill="#548235"/>
        <polygon points="145,407 252,355 252,460" fill="#8db070"/>
        <polygon points="252,355 359,407 252,460" fill="#669c45"/>
        <polygon points="145,567 252,620 252,678 145,625" fill="#a9d18e"/>
        <polygon points="252,620 359,567 359,625 252,678" fill="#a9d18e"/>
        <text class="t-column" x="244" y="637" text-anchor="middle">Minimum Reserve</text>
      </g>

      <g class="column column--insurance">
        <polygon points="484,245 591,300 591,678 484,625" fill="#fff0b3"/>
        <polygon points="591,300 698,245 698,625 591,678" fill="#ffe08a"/>
        <polygon points="591,195 698,245 591,300 484,245" fill="#bf9000"/>
        <polygon points="484,380 591,433 591,678 484,625" fill="#ffc000"/>
        <polygon points="591,433 698,380 698,625 591,678" fill="#bf9000"/>
        <polygon points="484,380 591,327 591,433" fill="#e0c472"/>
        <polygon points="591,327 698,380 591,433" fill="#dcb845"/>
        <text class="t-column" text-anchor="middle">
          <tspan x="591" y="465">Cash Value</tspan>
          <tspan x="591" y="488">continues to</tspan>
          <tspan x="591" y="511">grow</tspan>
          <tspan x="591" y="555">Can never lose</tspan>
          <tspan x="591" y="578">Principal</tspan>
          <tspan x="591" y="632">Cash Value</tspan>
        </text>
      </g>

      <g class="column column--heloc">
        <polygon points="821,245 928,300 928,678 821,625" fill="#b04040"/>
        <polygon points="928,300 1035,245 1035,625 928,678" fill="#8b4040"/>
        <polygon points="928,195 1035,245 928,300 821,245" fill="#c00000"/>
        <polygon points="821,545 928,598 928,678 821,625" fill="#990000"/>
        <polygon points="928,598 1035,545 1035,625 928,678" fill="#600000"/>
        <polygon points="821,545 928,493 928,598" fill="#a50000"/>
        <polygon points="928,493 1035,545 928,598" fill="#800000"/>
      </g>

      <g class="arrow">
        <polygon points="21,350 124,350 133,378 124,407 21,407" fill="var(--arrow-blue)"/>
        <polyline points="124,350 133,378 124,407" fill="none" stroke="var(--arrow-tip)" stroke-width="5"/>
        <text class="t-arrow" x="72" y="384" text-anchor="middle">Income</text>
      </g>
      <g class="arrow">
        <polygon points="21,427 124,427 133,455 124,483 21,483" fill="var(--arrow-blue)"/>
        <polyline points="124,427 133,455 124,483" fill="none" stroke="var(--arrow-tip)" stroke-width="5"/>
        <text class="t-arrow" x="72" y="461" text-anchor="middle">Income</text>
      </g>
      <g class="arrow">
        <polygon points="366,407 469,407 478,435 469,463 366,463" fill="var(--arrow-blue)"/>
        <polyline points="469,407 478,435 469,463" fill="none" stroke="var(--arrow-tip)" stroke-width="5"/>
        <text class="t-arrow" text-anchor="middle"><tspan x="418" y="431">Funds</tspan><tspan x="418" y="450">Transfer</tspan></text>
      </g>
      <g class="arrow">
        <polygon points="366,478 469,478 478,506 469,535 366,535" fill="var(--arrow-blue)"/>
        <polyline points="469,478 478,506 469,535" fill="none" stroke="var(--arrow-tip)" stroke-width="5"/>
        <text class="t-arrow" text-anchor="middle"><tspan x="418" y="502">Funds</tspan><tspan x="418" y="521">Transfer</tspan></text>
      </g>
      <g class="arrow arrow--ft">
        <polygon points="704,437 807,437 816,465 807,494 704,494" fill="var(--arrow-blue)"/>
        <polyline points="807,437 816,465 807,494" fill="none" stroke="var(--arrow-tip)" stroke-width="5"/>
        <text class="t-ft" x="755" y="475" text-anchor="middle">FT</text>
      </g>
      <g class="arrow arrow--purchase">
        <polygon points="1041,437 1144,437 1153,465 1144,494 1041,494" fill="var(--arrow-blue)"/>
        <polyline points="1144,437 1153,465 1144,494" fill="none" stroke="var(--arrow-tip)" stroke-width="5"/>
        <text class="t-arrow-sm" text-anchor="middle"><tspan x="1092" y="462">New Home</tspan><tspan x="1092" y="478">Purchase</tspan></text>
      </g>
    </g>

    <g class="column column--home">
      <polygon points="1159,245 1266,300 1266,678 1159,625" fill="#102460"/>
      <polygon points="1266,300 1373,245 1373,625 1266,678" fill="#0b1b48"/>
      <polygon points="1266,195 1373,245 1266,300 1159,245" fill="#0f2a6b"/>
      <rect x="1175" y="100" width="200" height="190" rx="30" fill="url(#house-tone)" role="img" aria-label="Illustration of a small house with trees, clouds and sun sitting on top of the column"/>
      <text class="t-home" text-anchor="middle">
        <tspan x="1266" y="412">New</tspan>
        <tspan x="1266" y="457">Home</tspan>
        <tspan x="1266" y="502">Purchase</tspan>
      </text>
    </g>
  </svg>
</section>

<section class="slide slide--second">
  <header class="slide-header">
    <h1 class="slide-title">Wealth Builder Account</h1>
    <div class="brand">Northwise Financial</div>
  </header>
  <svg class="flow" viewBox="0 0 1505 740" xmlns="http://www.w3.org/2000/svg">
    <use href="#shared-flow"/>
    <text class="t-home-label" text-anchor="middle">
      <tspan x="1266" y="137">New Home</tspan>
      <tspan x="1266" y="182">Purchase</tspan>
    </text>
    <g class="column column--home">
      <polygon points="1159,245 1266,300 1266,678 1159,625" fill="#102460"/>
      <polygon points="1266,300 1373,245 1373,625 1266,678" fill="#0b1b48"/>
      <polygon points="1266,195 1373,245 1266,300 1159,245" fill="#0f2a6b"/>
      <circle cx="1274" cy="468" r="143" fill="url(#bubble)"/>
      <rect x="1180" y="375" width="190" height="190" rx="40" fill="url(#house-tone)" role="img" aria-label="Illustration of a small house with trees, clouds and sun inside a round badge"/>
    </g>
  </svg>
</section>

</body>
</html>
```